Business Card design for insurance broker in Denver, CO, USA

I need a business card designed using this logo that was just created. We sell life and disability income insurance to US consumers.
Looking for a professionally designed card to make use of the logo and have something to hand to prospects or new business referral sources. The card could be white, gray, black or whatever you would recommend.

Target Market(s)

US Consumers and other financial professionals that I partner with.

Industry/Entity Type

Insurance Broker

Contact Information for Business Card

Owen R. Tessler, CLU, LUTCF (please note that CLU should have a superscript R in a circle for registered trademark)
President
phone (303) 555-0147
email owen@brightlakecoverage.com
4620 W. Hollister Rd, Suite 310, Greenwood Village, CO 80111
Somewhere fit in a tagline saying "Your resource for life, long term care, and disability insurance" (maybe the back if it doesn't fit on the front, your call)

Font styles to use
Sans Serif

Requirements
Must have
• Must have logo in correct blue and gray colors, my name, address, phone, email. Order and placement determined by the designer.
• I just want something that looks a more professional than what I could have done using the business card designer tool on printmakerhub.com or CardNest, or any other do-it-yourself tool
• A regular rectangular business card with square corners is preferred
Nice to have
• I included the logos of 2 organizations I belong to (GQLF and BEPWO). They should be small, but visible on the back only. If it doesn’t look good, this is not a requirement, feel free to drop it.
Should not have
• Do not add any colors not already in the logo, except use of black and whites which are okay. If you use the logo on the back and want to make that in all black, gray or white, that may be okay as well.

```html
<!DOCTYPE html>
<html lang="en">
<head>
<meta charset="utf-8">
<title>Brightlake Coverage – Business Card</title>
<link rel="stylesheet" href="https://fonts.googleapis.com/css2?family=Open+Sans:wght@400;600;700&display=swap">
<style>
  :root {
    --backdrop: #3b3531;
    --card: #17191c;
    --brand-blue: #1e8fd8;
    --brand-gray: #a3a6a9;
    --silver: #c9ccce;
    --ink-white: #eef0f1;
    --rule: #8d9094;
  }
  * { box-sizing: border-box; margin: 0; padding: 0; }
  html, body { width: 1200px; height: 864px; overflow: hidden; }
  body {
    background: var(--backdrop);
    font-family: "Open Sans", Arial, sans-serif;
    position: relative;
  }
  .card {
    position: absolute;
    background: var(--card);
    box-shadow: 0 10px 28px rgba(0,0,0,.45);
  }

  /* Back of card */
  .card-back { left: 60px; top: 70px; width: 560px; height: 320px; }
  .back-brand {
    position: absolute; left: 0; right: 0; top: 110px;
    display: flex; align-items: center; justify-content: center; gap: 14px;
  }
  .back-brand .dot {
    width: 30px; height: 30px; border-radius: 50%;
    border: 3px solid var(--silver);
  }
  .back-brand .name {
    color: var(--silver); font-weight: 600; font-size: 38px; letter-spacing: 2px;
  }
  .tagline {
    position: absolute; left: 40px; bottom: 42px;
    color: var(--ink-white); font-size: 13px;
  }
  .memberships {
    position: absolute; right: 34px; top: 30px;
    display: flex; gap: 16px; align-items: center;
  }
  .badge { background: var(--ink-white); }
  .badge-triangle { width: 38px; height: 30px; clip-path: polygon(50% 0, 100% 100%, 0 100%); }
  .badge-round { width: 34px; height: 34px; border-radius: 50%; }

  /* Front of card */
  .card-front { left: 560px; top: 440px; width: 600px; height: 343px; }
  .front-brand {
    position: absolute; left: 34px; top: 128px;
    display: flex; align-items: center; gap: 14px;
  }
  .front-brand .dot {
    width: 40px; height: 40px; border-radius: 50%;
    border: 4px solid var(--brand-blue);
  }
  .front-brand .name {
    color: var(--brand-blue); font-weight: 600; font-size: 23px;
    line-height: 1.05; letter-spacing: 1px;
  }
  .divider {
    position: absolute; left: 282px; top: 48px; width: 1px; height: 250px;
    background: linear-gradient(to bottom, transparent, var(--rule) 20%, var(--rule) 80%, transparent);
  }
  .contact { position: absolute; left: 306px; top: 76px; color: var(--ink-white); }
  .contact .person {
    color: var(--brand-blue); font-weight: 700; font-size: 17px; letter-spacing: .5px;
  }
  .contact .person small { font-size: 11px; }
  .contact .person sup { font-size: 7px; }
  .contact .role { font-size: 14px; margin-bottom: 12px; }
  .contact .address { font-size: 13px; line-height: 1.4; margin-bottom: 8px; }
  .contact .line {
    display: flex; align-items: center; gap: 8px; font-size: 13px; line-height: 1.6;
  }
  .contact svg { width: 12px; height: 12px; fill: var(--brand-blue); flex: none; }
  .contact svg.icon-mail { fill: none; stroke: var(--brand-blue); stroke-width: 2.5; }
</style>
</head>
<body>

<section class="card card-back" aria-label="Card back">
  <div class="memberships">
    <div class="badge badge-triangle" role="img" aria-label="BEPWO membership badge"></div>
    <div class="badge badge-round" role="img" aria-label="GQLF membership badge"></div>
  </div>
  <div class="back-brand">
    <span class="dot"></span>
    <span class="name">BRIGHTLAKE</span>
  </div>
  <p class="tagline">Your resource for life, long term care, &amp; disability insurance</p>
</section>

<section class="card card-front" aria-label="Card front">
  <div class="front-brand">
    <span class="dot"></span>
    <span class="name">BRIGHTLAKE<br>COVERAGE</span>
  </div>
  <div class="divider"></div>
  <div class="contact">
    <p class="person">OWEN R. TESSLER, <small>CLU<sup>®</sup>, LUTCF</small></p>
    <p class="role">CEO/FOUNDER</p>
    <p class="address">4620 W. Hollister Rd, Suite 310<br>Maple Ridge, CO 80274</p>
    <p class="line">
      <svg viewBox="0 0 24 24" aria-hidden="true"><path d="M6.6 10.8a15.1 15.1 0 0 0 6.6 6.6l2.2-2.2a1 1 0 0 1 1-.25 11.4 11.4 0 0 0 3.6.57 1 1 0 0 1 1 1V20a1 1 0 0 1-1 1A17 17 0 0 1 3 4a1 1 0 0 1 1-1h3.5a1 1 0 0 1 1 1c0 1.25.2 2.45.57 3.57a1 1 0 0 1-.25 1z"/></svg>
      (303) 555-0147
    </p>
    <p class="line">
      <svg class="icon-mail" viewBox="0 0 24 24" aria-hidden="true"><rect x="2" y="5" width="20" height="14"/><path d="M2 5l10 8 10-8"/></svg>
      owen@brightlakecoverage.com
    </p>
    <p class="line">
      <svg viewBox="0 0 24 24" aria-hidden="true"><circle cx="12" cy="12" r="10"/></svg>
      brightlakecoverage.com
    </p>
  </div>
</section>

</body>
</html>
```